Sehr angenehme und professionelle Zusammenarbeit!
Zielgruppe
Ich bin ein Consultant, der sich jetzt selbständig macht. Alles weitere steht in meinen Briefing. Dort findet ihr Fotos, mein Logo und damit auch die Farben, die ich mir wünsche. Meine Zielgruppe sind überwiegend Firmen, aber auch deren Mitarbeitende.
Aufgabenstellung
Die Struktur habe ich versucht zu beschreiben und hoffentlich auch alles über mich und mein Business. Ich freue mich auf eure kreativen und individuellen Vorschläge und bemühe mich zeitnah Feedback zu geben. Manchmal kann es den einen oder anderen Tag dauern. Bei Fragen gerne melden. Ich werde die Fragen, die für alle relevant sind auch im allgemeinen Kommentarfeld veröffentlichen.

```html
<!DOCTYPE html>
<html lang="de">
<head>
<meta charset="utf-8">
<title>Robert Thalmann – Beratung</title>
<link href="https://fonts.googleapis.com/css2?family=EB+Garamond:wght@400;600;700&family=Quicksand:wght@400;500;600;700&display=swap" rel="stylesheet">
<style>
:root{
  --navy:#123f8c;
  --ink:#1d1d1f;
  --muted:#6b6f78;
  --soft-bg:#f7f8fa;
  --line:#e6e8ec;
  --backdrop:#eceef2;
  --white:#ffffff;
}
*{margin:0;padding:0;box-sizing:border-box}
html,body{width:1200px;height:2402px;overflow:hidden;background:var(--white)}
body{position:relative;font-family:"Quicksand",sans-serif;color:var(--ink)}
.serif{font-family:"EB Garamond",serif}
.abs{position:absolute}
.btn{position:absolute;background:var(--navy);color:var(--white);font-size:10.5px;font-weight:600;display:flex;align-items:center;justify-content:center;text-decoration:none}

/* header */
.site-header{left:0;top:0;width:1200px;height:73px;background:var(--soft-bg);border-bottom:1px solid var(--line)}
.brand{left:41px;top:24px;display:flex;align-items:center;gap:10px;font-family:"EB Garamond",serif;font-size:20px;color:#333}
.brand-dot{width:24px;height:24px;border-radius:50%;background:var(--navy)}
.nav{right:0;top:22px;height:28px}
.nav a{position:absolute;top:6px;font-size:11.5px;color:var(--muted);text-decoration:none;white-space:nowrap}
.nav a.active{color:var(--ink)}

/* hero */
.hero{left:0;top:73px;width:1200px;height:395px;background:var(--soft-bg)}
.hero-title{left:195px;top:160px;font-size:37px;line-height:46px;color:var(--ink)}
.hero-title b{font-weight:700}
.hero-photo{left:607px;top:0;width:593px;height:395px;background:linear-gradient(100deg,#e9e8e5 0%,#c9c5c0 35%,#d9607f 70%,#e84a6d 100%)}
.slider-dots span{position:absolute;width:6px;height:6px;border-radius:50%;background:var(--white)}

.intro{left:195px;top:514px;width:812px;column-count:2;column-gap:14px;font-size:11.3px;line-height:16.3px}

/* win section */
.win-photo{left:0;top:695px;width:592px;height:395px;background:linear-gradient(160deg,#f1f2f3 0%,#d8dadd 50%,#2f4f8c 78%,#c9cbcf 100%)}
.win-title{left:640px;top:748px;font-size:37px;line-height:45px}
.win-text{left:640px;top:859px;width:368px;font-size:11.3px;line-height:16.3px}

/* offers */
.offers-title{left:195px;top:1130px;font-size:38px;font-weight:700}
.offers-rule{left:508px;top:1164px;width:692px;height:1px;background:var(--line)}
.offer{position:absolute;top:1222px;width:241px;height:329px}
.offer-card{background:var(--soft-bg);box-shadow:0 2px 6px rgba(0,0,0,.08)}
.offer-card .photo{height:179px;background:linear-gradient(180deg,#6f8a5f,#9fae8c 60%,#8fa3c4)}
.offer-card h3{font-family:"EB Garamond",serif;font-weight:600;font-size:20px;line-height:26px;margin:15px 0 0 15px}
.offer-card p{font-size:11px;color:var(--muted);margin:6px 0 0 15px}

/* about */
.about-backdrop{left:220px;top:1739px;width:363px;height:473px;background:var(--backdrop)}
.about-photo{left:196px;top:1705px;width:361px;height:485px;background:linear-gradient(180deg,#e3e1de 0%,#d9c4b0 45%,#b7cbe6 78%,#25375e 100%)}
.about-title{left:640px;top:1704px;font-size:38px;line-height:45px}
.about-title b{font-weight:700}
.about-text{left:640px;top:1903px;width:370px;font-size:11.3px;line-height:16.3px}
.about-text h4{font-weight:700;font-size:11.3px}
.about-text p{margin-bottom:16px}
</style>
</head>
<body>

<header class="site-header abs">
  <div class="brand abs"><span class="brand-dot"></span><span>Robert Thalmann</span></div>
  <nav class="nav abs">
    <a class="active" style="left:-292px">Home</a>
    <a style="left:-245px">Angebote</a>
    <a style="left:-177px">Über mich</a>
  </nav>
  <a class="btn" style="left:1093px;top:22px;width:66px;height:28px;font-size:11.5px">Kontakt</a>
</header>

<section class="hero abs">
  <h1 class="hero-title serif abs"><b>Für alle. Das Beste.</b><br><span style="font-weight:400">Beratung für komplexe<br>Personal-situationen.</span></h1>
  <div class="hero-photo abs" role="img" aria-label="Foto: Berater im Gespräch mit einer Kollegin, farbige Bewegungsunschärfe rechts"></div>
  <div class="slider-dots"><span style="left:1174px;top:171px"></span><span style="left:1174px;top:189px"></span><span style="left:1174px;top:207px"></span></div>
</section>

<div class="intro abs">
Personalprobleme sind eine normale Begleiterscheinung in unserer Zeit voll Wandel. Im Daily Business werden diese Situationen jedoch selten tiefer analysiert und häufig nur kosmetisch behandelt. Ein Aussitzen hier, eine Mediation dort, ein plötzliches Abfindungsangebot da. Vielleicht auch schon zahlreiche Gespräche oder Coachings, die nicht zur gewünschten Veränderung führten.<br>Die Folge: die Motivation sinkt. Nicht nur bei dem/der jeweiligen Mitarbeitenden, auch im Teamumfeld und bei der Führungskraft. Frustration steigt, es kommt zu Fehlzeiten, die Produktivität lässt nach, mitunter können Ziele nicht erreicht werden. Die Gerüchteküche köchelt vor sich hin.<br>Meine Beratung und Prozessbegleitung schließt hier eine Lücke. Sie bietet nachhaltige Lösungen bei komplexen und dysfunktionalen Personalsituationen an, die alle Seiten einbeziehen: Mitarbeitende/r. Führungskraft. Organisation.
</div>

<section>
  <div class="win-photo abs" role="img" aria-label="Foto: Mann im blauen Anzug jubelt mit erhobenen Armen unter einer weißen Brückenkonstruktion"></div>
  <div class="slider-dots"><span style="left:18px;top:861px"></span><span style="left:18px;top:879px"></span><span style="left:18px;top:897px"></span></div>
  <h2 class="win-title serif abs"><span style="font-weight:400">Von Lose zu </span><b>Win<br>für alle Seiten.</b></h2>
  <p class="win-text abs">Während auf individueller Ebene Menschen ihr Potenzial nicht entfalten können und oft lange an der Situation leiden, entstehen auf organisationaler Ebene wirtschaftliche Einbußen und Imageschäden. Selten ist nur eine Person betroffen, auch wenn es sich oft auf eine Person fokussiert. Die Ursachen sind multifaktoriell und langwierig, die negative Wirkung strahlt auf den/die Mitarbeitende/n, die Führungskraft, das Team und die Abteilung aus.</p>
  <a class="btn" style="left:640px;top:1011px;width:144px;height:26px">Zum Kennenlerngespräch</a>
</section>

<section>
  <h2 class="offers-title serif abs">Meine Angebote</h2>
  <div class="offers-rule abs"></div>
  <article class="offer offer-card" style="left:195px">
    <div class="photo" role="img" aria-label="Foto: zwei Männer im Gespräch am Flussufer"></div>
    <h3>Prozessberatung<br>und – begleitung</h3>
    <p>Ganzheitlich vom Problem zur Lösung</p>
    <a class="btn" style="left:15px;top:286px;width:59px;height:26px">Mehr</a>
  </article>
  <div class="offer" style="left:450px;background:linear-gradient(180deg,#7a8a5c,#b9c9de 60%,#5a6f96)" role="img" aria-label="Foto: Berater im Gespräch, im Freien sitzend"></div>
  <div class="offer" style="left:704px;height:326px;background:linear-gradient(180deg,#3b4252,#8b8a85 55%,#a7a39b)" role="img" aria-label="Foto: zwei Personen gehen einen Kiesweg entlang"></div>
  <div class="offer" style="left:959px;background:linear-gradient(180deg,#b9a38c,#c8d4e4 60%,#9bb6da)" role="img" aria-label="Foto: lächelnder Berater im hellblauen Hemd vor Altstadtkulisse"></div>
</section>

<section>
  <div class="about-backdrop abs"></div>
  <div class="about-photo abs" role="img" aria-label="Porträtfoto des Beraters mit Brille im dunkelblauen Sakko"></div>
  <h2 class="about-title serif abs"><span style="font-weight:400">Ich bin </span><b>Robert<br>Thalmann</b><span style="font-weight:400"> und mein<br>Anspruch ist: </span><b>Für<br>alle. Das Beste.</b></h2>
  <div class="about-text abs">
    <h4>Meine Motivation:</h4>
    <p>Ich möchte Menschen unterstützen, sich aus dysfunktionalen Arbeitssituationen zu lösen, ihr Potenzial zu erkennen und auszuleben. Dafür setze ich mich als selbstständiger Berater ein, nach 25 Jahren im Personalbereich, zumeist in Führungspositionen.</p>
    <h4>Meine Überzeugung:</h4>
    <p>Weil es immer eine bessere Lösung gibt, strebe ich Win-Win-Win-Lösungen an. Und das unheimlich gerne. Für den Menschen und fürs Unternehmen. Menschlich und wirtschaftlich.</p>
    <h4>Meine Haltung:</h4>
    <p>Vor ein paar Jahren während meiner Zeit als Leiter der Personalentwicklung sagte ein Personalvorstand mal ganz lakonisch im fränkischen Dialekt: „Am Ende geht’s darum, sauba mit die Leut‘ umgehn.“ Dem habe ich nichts hinzuzufügen.</p>
  </div>
  <a class="btn" style="left:640px;top:2185px;width:97px;height:26px">Mehr über mich</a>
</section>

</body>
</html>
```